900mm double sided Card Ponytail Insert for hair

I need print ready file designs for card packaging inserts for my line of ponytails, These are two sided colour and fold at each end or contain the hair, for structure and so the brand is on display. These will be marketed as luxury ponytails, so we want a simple, soft but luxurious design feel. All the details are below but it will be the logo, photos and simple messaging

Target Market(s)

18-30 females

Industry/Entity Type

Beauty

Font styles to use
Serif

Requirements
Must have
• - Lumera Logo on the back and top front fold.
'Luxury Synthetic Ponytails' Head line
'For effortlessly long and luxurious hair' tag line
'For tutorials, questions and inspiration head to our 'Brightroom' on lumerabeauty.com'
www.lumerabeauty.com
Tag us on socials! @lumerabeautyofficial (pictavo and Chatterloop logos)
3 step-by-step pictures (holding pictures please until i have some taken)
Nice to have
• (notes to designers) view our website to see our branding lumerabeauty.com - it would be good to use our brand colours and somekind of tropical leaves maybe? i'm thinking palm leaves?
- my brand font is Sweet Getaway - but this may only be good for the biggest headings

```html
<!DOCTYPE html>
<html lang="en">
<head>
<meta charset="utf-8">
<title>Lumera Ponytail Insert</title>
<link rel="stylesheet" href="https://fonts.googleapis.com/css2?family=Questrial&family=Mulish:wght@700;800&family=League+Spartan:wght@700&display=swap">
<style>
  :root {
    --gold: #e2b354;
    --gold-text: #d6a24a;
    --ink: #333333;
    --body: #3d3d3d;
    --white: #ffffff;
    --leaf: #e4f1ec;
    --blush: #f7d7de;
    --step-tone: #efe4d2;
  }
  * { margin: 0; padding: 0; box-sizing: border-box; }
  html, body { width: 1200px; height: 849px; overflow: hidden; background: var(--white); }
  .insert { position: relative; width: 1200px; height: 849px; background: var(--white); overflow: hidden; font-family: "Questrial", sans-serif; }

  /* Front panel */
  .panel-front { position: absolute; left: 0; top: 0; width: 599px; height: 849px; background: var(--gold); overflow: hidden; }
  .model-backdrop { position: absolute; left: 60px; top: 80px; width: 520px; height: 769px;
    background: radial-gradient(ellipse at 50% 40%, rgba(240,200,110,0.55), rgba(226,179,84,0) 70%); }
  .rule-vertical { position: absolute; left: 48px; top: 0; width: 2px; height: 849px; background: var(--white); }
  .rule-horizontal { position: absolute; left: 0; top: 84px; width: 203px; height: 2px; background: var(--white); }

  .tutorial-kicker { position: absolute; left: 72px; top: 52px; font-size: 24px; color: var(--white); }
  .tutorial-line { position: absolute; left: 72px; top: 90px; font-size: 24px; color: var(--white); letter-spacing: 0.3px; }
  .zone-title { position: absolute; left: 70px; top: 120px; font-family: "League Spartan", sans-serif; font-weight: 700;
    font-size: 57px; line-height: 1; color: var(--ink); letter-spacing: 1px; }
  .zone-site { position: absolute; left: 72px; top: 170px; font-size: 24px; color: var(--white); letter-spacing: 0.4px; }

  .blog-title { position: absolute; left: 72px; top: 231px; font-family: "Mulish", sans-serif; font-weight: 800; font-size: 15.5px; color: var(--ink); }
  .blog-excerpt { position: absolute; left: 69px; top: 266px; width: 445px; font-size: 15.5px; line-height: 31.6px; color: var(--white); letter-spacing: 0.2px; }

  .photo { position: absolute; top: 473px; width: 223px; height: 309px; }
  .photo-model { left: 71px; background: linear-gradient(160deg, #d9dbe6 0%, #c9b7bd 45%, #3a2f35 100%); }
  .photo-lace { left: 305px; background: linear-gradient(200deg, #1f1a18 0%, #3b302b 45%, #c9a79f 80%, #e7cfc8 100%); }

  /* Back panel */
  .panel-back { position: absolute; left: 599px; top: 0; width: 601px; height: 849px; overflow: hidden; }
  .leaf-decor { position: absolute; left: 185px; top: 410px; width: 420px; height: 439px;
    background: radial-gradient(ellipse at 55% 50%, rgba(228,241,236,0.85), rgba(255,255,255,0) 70%); }
  .leaf-accent { position: absolute; left: 350px; top: 445px; width: 90px; height: 90px;
    background: radial-gradient(circle, rgba(247,215,222,0.7), rgba(255,255,255,0) 70%); }

  .brand { position: absolute; left: 82px; top: 56px; display: flex; align-items: center; gap: 10px; }
  .brand-dot { width: 14px; height: 14px; border-radius: 50%; background: var(--gold-text); }
  .brand-name { font-family: "Mulish", sans-serif; font-weight: 800; font-size: 26px; letter-spacing: 6px; color: var(--gold-text); }

  .headline { position: absolute; left: 82px; top: 118px; font-family: "Mulish", sans-serif; font-weight: 800; font-size: 31px; line-height: 1; color: var(--gold-text); }
  .tagline { position: absolute; left: 82px; top: 166px; font-size: 18px; color: var(--body); letter-spacing: 0.3px; }

  .steps { position: absolute; left: 82px; top: 226px; width: 440px; display: flex; gap: 18px; }
  .step { width: 134px; }
  .step-photo { width: 134px; height: 190px; background: linear-gradient(170deg, var(--step-tone) 0%, #e7c98f 100%); }
  .step-label { margin-top: 12px; font-family: "Mulish", sans-serif; font-weight: 800; font-size: 15px; color: var(--gold-text); }
  .step-text { margin-top: 4px; font-size: 14px; line-height: 20px; color: var(--body); }

  .contact { position: absolute; left: 82px; top: 560px; width: 440px; }
  .contact-site { font-family: "Mulish", sans-serif; font-weight: 800; font-size: 20.5px; color: var(--gold-text); }
  .contact-social { margin-top: 22px; font-size: 16px; color: var(--body); }
  .contact-handle { margin-top: 6px; font-size: 18px; color: var(--ink); }
  .networks { margin-top: 16px; display: flex; gap: 28px; }
  .network { display: flex; align-items: center; gap: 8px; font-size: 16px; color: var(--body); }
  .network-dot { width: 10px; height: 10px; border-radius: 50%; background: var(--gold-text); }
</style>
</head>
<body>
<main class="insert">
  <section class="panel-front">
    <div class="model-backdrop" role="img" aria-label="Faded portrait photograph of a model with long hair"></div>
    <div class="rule-vertical"></div>
    <div class="rule-horizontal"></div>
    <p class="tutorial-kicker">For Tutorials:</p>
    <p class="tutorial-line">questions and inspiration head to our</p>
    <h2 class="zone-title">BRIGHTROOM</h2>
    <p class="zone-site">on lumerabeauty.com</p>
    <h3 class="blog-title">A guide to wearing a wig with alopecia - A Guest Blog.</h3>
    <p class="blog-excerpt">In recent months we have stocked wigs that are synthetic but are not lace front wigs, you may have noticed them- because of the price difference listed on our site. So what's the difference and should you purchase one? 1. What is a lace front wig? A wig is called lace front..</p>
    <div class="photo photo-model" role="img" aria-label="Photograph of a model wearing a long ash blonde ombre wig"></div>
    <div class="photo photo-lace" role="img" aria-label="Close-up photograph of a lace front wig hairline"></div>
  </section>

  <section class="panel-back">
    <div class="leaf-decor" role="img" aria-label="Faint tropical palm leaf decoration"></div>
    <div class="leaf-accent" role="img" aria-label="Faint pink lips print decoration"></div>

    <div class="brand"><span class="brand-dot"></span><span class="brand-name">LUMERA</span></div>
    <h1 class="headline">Luxury Synthetic Ponytails</h1>
    <p class="tagline">For effortlessly long and luxurious hair</p>

    <div class="steps">
      <div class="step">
        <div class="step-photo" role="img" aria-label="Step one photograph placeholder"></div>
        <p class="step-label">Step 1</p>
        <p class="step-text">Tie your hair into a secure base.</p>
      </div>
      <div class="step">
        <div class="step-photo" role="img" aria-label="Step two photograph placeholder"></div>
        <p class="step-label">Step 2</p>
        <p class="step-text">Clip the ponytail over the base.</p>
      </div>
      <div class="step">
        <div class="step-photo" role="img" aria-label="Step three photograph placeholder"></div>
        <p class="step-label">Step 3</p>
        <p class="step-text">Wrap and pin to hide the join.</p>
      </div>
    </div>

    <div class="contact">
      <p class="contact-site">www.lumerabeauty.com</p>
      <p class="contact-social">Tag us on socials!</p>
      <p class="contact-handle">@lumerabeautyofficial</p>
      <div class="networks">
        <span class="network"><span class="network-dot"></span>pictavo</span>
        <span class="network"><span class="network-dot"></span>Chatterloop</span>
      </div>
    </div>
  </section>
</main>
</body>
</html>
```